Stationary Package
Business Card / Letterhead / Envelop
I need double sided standard sized Business Card [3.5" x 2"]
use same look and feel font(s)
Professional
Daniel Whitfield
Marketing Strategist
4518 Harwick Crescent
Mississauga, Ontario, L4T 3K8
danielwhitfield@vellorahaus.com
www.vellorahaus.com
design package for the marketing industry
Logo with tag line
plus the website address
Logo and Tag Line
eps logo
pdf logo version

```html
<!DOCTYPE html>
<html lang="en">
<head>
<meta charset="utf-8">
<title>Daniel Whitfield – Business Card</title>
<link href="https://fonts.googleapis.com/css2?family=Open+Sans:ital,wght@0,400;0,600;0,700;1,700&display=swap" rel="stylesheet">
<style>
  :root{
    --bg:#e9e9ec;
    --card:#ffffff;
    --navy:#1c2478;
    --blue:#2e46b8;
    --sky:#4a6fd8;
    --swoosh:#dcdfe6;
    --ink:#2b2b3a;
    --white:#ffffff;
  }
  *{margin:0;padding:0;box-sizing:border-box}
  html,body{width:1200px;height:427px;overflow:hidden;background:var(--bg);font-family:"Open Sans",Arial,sans-serif}
  .sheet{position:relative;width:1200px;height:427px}
  .card{position:absolute;top:80px;width:460px;height:266px;border-radius:14px;overflow:hidden;background:var(--card);box-shadow:0 2px 6px rgba(0,0,0,.18)}
  .card--front{left:118px}
  .card--back{left:622px}
  .card svg.card-art{position:absolute;inset:0;width:100%;height:100%}
  .brand{position:absolute;display:flex;align-items:center;gap:8px;color:var(--navy);font-weight:700;letter-spacing:.3px;white-space:nowrap}
  .brand__dot{width:20px;height:20px;border-radius:50%;background:var(--blue);flex:none}
  .card--front .brand{left:26px;top:62px;font-size:18px}
  .card--back .brand{left:50%;top:96px;transform:translateX(-50%);font-size:30px;gap:12px}
  .card--back .brand__dot{width:32px;height:32px}
  .contact{position:absolute;left:196px;top:88px;list-style:none;font-size:8px;color:var(--ink);line-height:12.5px;white-space:nowrap}
  .contact li{display:flex;align-items:flex-start;gap:5px}
  .contact li::before{content:"";width:5px;height:5px;margin-top:4px;border-radius:50%;background:var(--blue);flex:none}
  .contact .cont{padding-left:10px}
  .contact .cont::before{display:none}
  .person{position:absolute;left:24px;top:212px;color:var(--white)}
  .person__name{font-size:15px;font-weight:700;letter-spacing:.4px}
  .person__role{font-size:11px;font-weight:400;margin-top:1px}
  .tagline{position:absolute;left:24px;bottom:22px;color:var(--white);font-size:15px;font-weight:700;font-style:italic;white-space:nowrap}
</style>
</head>
<body>
<main class="sheet">

  <section class="card card--front" aria-label="Card front">
    <svg class="card-art" viewBox="0 0 460 266" aria-hidden="true">
      <defs>
        <linearGradient id="front-blue" x1="0" y1="1" x2="1" y2="0">
          <stop offset="0" stop-color="#1c2478"/>
          <stop offset=".6" stop-color="#2e46b8"/>
          <stop offset="1" stop-color="#4a6fd8"/>
        </linearGradient>
      </defs>
      <path d="M270 0 C340 20 420 50 460 90 L460 0Z" fill="#eef0f4"/>
      <path d="M0 186 C240 202 420 176 460 70 L460 266 L0 266Z" fill="#dcdfe6"/>
      <path d="M0 198 C240 214 420 190 460 92 L460 266 L0 266Z" fill="url(#front-blue)"/>
    </svg>
    <div class="brand"><span class="brand__dot"></span>Vellora Haus</div>
    <ul class="contact">
      <li>4518 Harwick Crescent</li>
      <li class="cont">Mississauga, Ontario, L4T 3K8</li>
      <li>416 555 0187</li>
      <li>danielwhitfield@vellorahaus.com</li>
      <li>www.vellorahaus.com</li>
    </ul>
    <div class="person">
      <p class="person__name">DANIEL WHITFIELD</p>
      <p class="person__role">Marketing Strategist</p>
    </div>
  </section>

  <section class="card card--back" aria-label="Card back">
    <svg class="card-art" viewBox="0 0 460 266" aria-hidden="true">
      <defs>
        <linearGradient id="back-blue" x1="0" y1="0" x2="1" y2="1">
          <stop offset="0" stop-color="#1c2478"/>
          <stop offset="1" stop-color="#3556c8"/>
        </linearGradient>
      </defs>
      <path d="M0 0 L250 0 C170 18 70 60 0 140Z" fill="#dcdfe6"/>
      <path d="M0 0 L230 0 C150 18 60 62 0 126Z" fill="url(#back-blue)"/>
      <path d="M0 214 C170 206 360 186 460 110 L460 266 L0 266Z" fill="#dcdfe6"/>
      <path d="M0 226 C170 218 370 196 460 128 L460 266 L0 266Z" fill="url(#back-blue)"/>
    </svg>
    <div class="brand"><span class="brand__dot"></span>Vellora Haus</div>
    <p class="tagline">We are in the marketing industry</p>
  </section>

</main>
</body>
</html>
```